Need A Modern Website Design For ADSL2+ Provider

AIM: To sell affordable combined ADSL2+ Unlimited & phone line rentals to residential customers.

TYPE: This project is for DESIGN only (no code)

Source Files: I need all source files, fonts, images to be provided in ZIP format.

Logo: Existing (attached)

-Corporate Colours-
Black & Red (Same as Logo)
Others colours are fine as long as it looks corporate and modern.

-Pages-
Need another page to display our pricing plan

(1)Homepage Design
(2)Page to display our plans (needs to be in tables)
Example: http://lnkshrt.example/Qv7Rp2

-Pricing Plan-
(1) $59.95 / Month (Metro / City Areas)
(2) $79.95 / Month (Outside City Areas / Rural Areas)
Detailed Pricing plans is in PDF attached
Updates

Just letting everyone know we have picked a designer, thank you for all you submissions.

Target Market(s)

Both male & female, Young & Old

Industry/Entity Type

Residential

Requirements
Must have
• + Graphic banner on the home page that shows our ADSL2+ combo plan for ADSL2+ Unlimited & Phone Line Rental for only $59.95

+ A box to allow customers to login to their account (username & password + login button)

+ Clearly display contact number
+ Button to sign up
+ Button to check service availability something like https://linkup.vexora.com/wizard/

+ Button for Live Chat
+ Navigation menu
+ Social media icons Chatterly, Plexo +, Chirpnet
+ Minimal text on homepage
+ Corporate & Friendly
Nice to have
• + Effective use of icons with corporate colours
+ Effective use of stockphotos
(use of people in photos would be nice)

+ Effective use of graphics to navigate people through the site and inform customers of specials,etc.
Should not have
• + Cluttered
+ Don’t want long scrolling homepage
+ Don’t want too much text on homepage 500 words is the estimate max.

```html
<!DOCTYPE html>
<html lang="en">
<head>
<meta charset="utf-8">
<title>Veltra – ADSL2+ &amp; Phone Line</title>
<link href="https://fonts.googleapis.com/css2?family=Arimo:wght@400;700&family=Anton&display=swap" rel="stylesheet">
<style>
  :root {
    --red: #d0312d;
    --red-dark: #9b1424;
    --black: #1f1d1e;
    --ink: #1b1b1b;
    --grey-text: #5a5a5a;
    --page: #f6f6f6;
    --white: #ffffff;
    --field: #b5b5b5;
    --rule: #c9c9c9;
  }
  * { box-sizing: border-box; margin: 0; padding: 0; }
  html, body { width: 1174px; height: 1200px; overflow: hidden; }
  body {
    position: relative;
    background: var(--page);
    font-family: "Arimo", Helvetica, Arial, sans-serif;
    color: var(--ink);
  }

  /* Header */
  .site-header {
    position: absolute; left: 0; top: 0; width: 1174px; height: 99px;
    background: var(--white);
    box-shadow: 0 4px 10px rgba(0,0,0,0.08);
  }
  .brand {
    position: absolute; left: 135px; top: 21px;
    display: flex; align-items: center; gap: 12px;
  }
  .brand-mark { width: 52px; height: 52px; border-radius: 50%; background: var(--black); }
  .brand-name { font-size: 38px; font-weight: 400; letter-spacing: 1px; color: var(--black); }
  .header-actions { position: absolute; right: 134px; top: 34px; display: flex; gap: 7px; }
  .action-btn {
    height: 34px; padding: 0 12px 0 10px; border-radius: 3px;
    display: flex; align-items: center; gap: 8px;
    color: var(--white); font-size: 16px; font-weight: 700;
    box-shadow: 0 2px 0 rgba(0,0,0,0.25);
  }
  .action-btn svg { width: 20px; height: 20px; }
  .action-signup { background: var(--red); width: 106px; }
  .action-login { background: #8e8e8e; width: 91px; }
  .action-chat { background: #3a3a3a; width: 114px; }

  /* Main frame */
  .main-nav {
    position: absolute; left: 135px; top: 135px; width: 904px; height: 48px;
    background: var(--black); display: flex; align-items: center;
  }
  .nav-link { height: 48px; padding: 0 14px; display: flex; align-items: center; color: var(--white); font-size: 16px; font-weight: 700; }
  .nav-link.is-active { background: var(--red); padding: 0 21px; }
  .nav-phone { margin-left: auto; color: var(--white); font-size: 23px; margin-right: 12px; }
  .social { display: flex; gap: 4px; margin-right: 11px; }
  .social-icon { width: 26px; height: 26px; border-radius: 2px; }
  .social-chatterly { background: #3b5998; }
  .social-plexo { background: #d2402f; }
  .social-chirpnet { background: #2aa6df; }

  .hero {
    position: absolute; left: 135px; top: 183px; width: 904px; height: 349px;
    background: linear-gradient(100deg, #9fb08e 0%, #d8dcd2 35%, #c7c9c2 55%, #3a3f4c 80%, #1e2535 100%);
  }
  .hero-caption {
    position: absolute; left: 0; top: 161px; width: 487px; height: 96px;
    background: rgba(255,255,255,0.88); padding: 12px 0 0 28px;
  }
  .hero-kicker { font-size: 29px; font-weight: 700; color: var(--ink); line-height: 1.1; }
  .hero-title { font-size: 47px; font-weight: 400; color: var(--red); line-height: 1.05; }
  .hero-dots { position: absolute; right: 10px; bottom: 9px; display: flex; gap: 4px; }
  .hero-dot { width: 13px; height: 13px; border-radius: 50%; background: var(--white); }
  .hero-dot.is-active { background: var(--red); }

  .service-band { position: absolute; left: 135px; top: 532px; width: 904px; height: 163px; box-shadow: 0 6px 12px rgba(0,0,0,0.12); }
  .availability { position: absolute; left: 0; top: 0; width: 644px; height: 163px; background: var(--red); color: var(--white); }
  .agent-photo {
    position: absolute; left: 0; top: -30px; width: 149px; height: 193px;
    background: linear-gradient(180deg, #6b4a36 0%, #c79b82 45%, #f1ece8 100%);
  }
  .availability-title { position: absolute; left: 153px; top: 14px; font-size: 23px; font-weight: 400; }
  .phone-field {
    position: absolute; left: 155px; top: 51px; width: 355px; height: 36px;
    background: var(--white); border-radius: 3px; display: flex; align-items: center; padding-left: 10px; gap: 12px;
    color: #9a9a9a; font-size: 17px;
  }
  .phone-field svg { width: 24px; height: 24px; }
  .browse-btn {
    position: absolute; left: 517px; top: 51px; width: 107px; height: 36px; border-radius: 3px;
    background: #000; color: var(--white); font-size: 20px; font-weight: 700;
    display: flex; align-items: center; justify-content: center;
  }
  .consent { position: absolute; left: 156px; top: 94px; font-size: 13.5px; line-height: 15px; width: 400px; }
  .opt-out { position: absolute; left: 156px; top: 131px; font-size: 13px; display: flex; align-items: center; gap: 6px; }
  .opt-out-box { width: 14px; height: 14px; background: var(--white); border-radius: 2px; }

  .login-panel { position: absolute; left: 644px; top: 0; width: 260px; height: 163px; background: var(--black); color: var(--white); }
  .login-title { position: absolute; left: 21px; top: 14px; font-size: 23px; font-weight: 400; }
  .login-field { position: absolute; left: 21px; width: 216px; height: 26px; background: var(--field); border-radius: 3px; }
  .login-user { top: 48px; }
  .login-pass { top: 82px; }
  .login-btn {
    position: absolute; left: 171px; top: 115px; width: 64px; height: 27px; border-radius: 3px;
    background: var(--red); color: var(--white); font-size: 16px;
    display: flex; align-items: center; justify-content: center;
  }

  /* Welcome */
  .welcome { position: absolute; left: 135px; top: 736px; width: 620px; }
  .welcome-title { font-size: 29px; font-weight: 400; color: var(--ink); }
  .welcome-title span { color: var(--red); }
  .welcome-lead { margin-top: 6px; font-size: 16.5px; font-weight: 700; line-height: 19px; }
  .welcome-body { margin-top: 14px; font-size: 14px; line-height: 18px; color: var(--grey-text); }
  .welcome-body + .welcome-body { margin-top: 18px; }

  .promo {
    position: absolute; left: 779px; top: 746px; width: 261px; height: 227px; border-radius: 3px; overflow: hidden;
    background: radial-gradient(circle at 40% 40%, #b41e32 0%, #8e0f22 70%);
    font-family: "Anton", "Arimo", sans-serif; color: var(--white); text-transform: uppercase;
  }
  .promo-line { position: absolute; left: 10px; line-height: 1; }
  .promo-l1 { top: 16px; font-size: 30px; }
  .promo-l2 { top: 46px; font-size: 30px; }
  .promo-l3 { top: 78px; font-size: 22px; }
  .promo-l4 { top: 100px; font-size: 22px; }
  .promo-l5 { top: 122px; font-size: 22px; }
  .promo-strip { position: absolute; left: 0; top: 146px; width: 261px; height: 53px; background: rgba(40,0,8,0.45); }
  .promo-price { top: 150px; font-size: 46px; color: #ff4a55; }
  .promo-cta { position: absolute; right: 12px; bottom: 4px; font-size: 18px; letter-spacing: 1px; }
  .promo-device { position: absolute; right: 10px; top: 58px; width: 92px; height: 120px; border-radius: 4px; background: linear-gradient(90deg, #3b3b3b, #777 60%, #c6c6c6); }

  /* Footer */
  .footer-rule { position: absolute; left: 135px; top: 1030px; width: 904px; height: 4px; border-top: 1px solid var(--rule); border-bottom: 1px solid var(--rule); }
  .footer-nav { position: absolute; left: 0; top: 1064px; width: 1174px; display: flex; justify-content: center; font-size: 13px; color: #333; }
  .footer-nav a { color: inherit; text-decoration: none; }
  .footer-nav a.is-active { color: var(--red); }
  .footer-nav .sep { margin: 0 8px; color: #aaa; }
  .footer-brand { position: absolute; left: 0; top: 1096px; width: 1174px; display: flex; justify-content: center; align-items: center; gap: 6px; color: #bdbdbd; font-size: 21px; }
  .footer-brand-mark { width: 28px; height: 28px; border-radius: 50%; background: #c6c6c6; }
  .copyright { position: absolute; left: 0; top: 1136px; width: 1174px; text-align: center; font-size: 13px; color: #333; }
  .bottom-bar { position: absolute; left: 0; top: 1196px; width: 1174px; height: 4px; background: var(--red); }
</style>
</head>
<body>

<header class="site-header">
  <div class="brand">
    <div class="brand-mark"></div>
    <div class="brand-name">VELTRA</div>
  </div>
  <div class="header-actions">
    <div class="action-btn action-signup">
      <svg viewBox="0 0 20 20"><circle cx="10" cy="6" r="4" fill="#fff"/><path d="M3 19c0-5 3-7 7-7s7 2 7 7z" fill="#fff"/></svg>Sign Up</div>
    <div class="action-btn action-login">
      <svg viewBox="0 0 20 20"><circle cx="10" cy="6" r="4" fill="#fff"/><path d="M3 19c0-5 3-7 7-7s7 2 7 7z" fill="#fff"/></svg>Login</div>
    <div class="action-btn action-chat">
      <svg viewBox="0 0 20 20"><ellipse cx="10" cy="9" rx="9" ry="7" fill="#7cc6ee"/><path d="M5 14l-2 5 6-3z" fill="#7cc6ee"/></svg>Live Chat</div>
  </div>
</header>

<nav class="main-nav">
  <span class="nav-link is-active">Home</span>
  <span class="nav-link">About Us</span>
  <span class="nav-link">Our Plans</span>
  <span class="nav-link">Contact Us</span>
  <span class="nav-phone">Call Us: 000-000-0000</span>
  <div class="social">
    <span class="social-icon social-chatterly" aria-label="Chatterly"></span>
    <span class="social-icon social-plexo" aria-label="Plexo +"></span>
    <span class="social-icon social-chirpnet" aria-label="Chirpnet"></span>
  </div>
</nav>

<section class="hero" role="img" aria-label="Photo of a smiling businessman talking on a mobile phone outdoors">
  <div class="hero-caption">
    <div class="hero-kicker">Sed lacinia vulputate dolor</div>
    <div class="hero-title">Praesent leo magna</div>
  </div>
  <div class="hero-dots">
    <span class="hero-dot is-active"></span><span class="hero-dot"></span><span class="hero-dot"></span><span class="hero-dot"></span>
  </div>
</section>

<section class="service-band">
  <div class="availability">
    <div class="agent-photo" role="img" aria-label="Photo of a support agent wearing a headset"></div>
    <h2 class="availability-title">Check service availability</h2>
    <div class="phone-field">
      <svg viewBox="0 0 24 24"><path d="M6 2l4 4-2 3c1 3 4 6 7 7l3-2 4 4-3 4C10 22 2 14 2 5z" fill="#8a8a8a"/></svg>
      Enter your phone number
    </div>
    <div class="browse-btn">Browse</div>
    <p class="consent">By entering a number you agree that we may contact you to discuss the availability of services in your area.</p>
    <div class="opt-out"><span class="opt-out-box"></span>Don't Call me</div>
  </div>
  <div class="login-panel">
    <h2 class="login-title">Login</h2>
    <div class="login-field login-user"></div>
    <div class="login-field login-pass"></div>
    <div class="login-btn">Login</div>
  </div>
</section>

<section class="welcome">
  <h1 class="welcome-title"><span>Welcome to</span> Veltra</h1>
  <p class="welcome-lead">Nam quis ligula a nibh fermentum venenatis vitae nec neque. Etiam non felis mi. Quisque feugiat, lectus non feugiat consectetur,</p>
  <p class="welcome-body">Aenean dapibus lorem laoreet ante pharetra ornare malesuada orci ornare. Ut volutpat ipsum ipsum, eget suscipit mauris. Sed sed nisl ac justo rutrum convallis. Fusce facilisis, nunc et viverra iaculis, arcu augue tempor ipsum,</p>
  <p class="welcome-body">ut auctor sapien justo ac metus. Morbi adipiscing sodales condimentum. Nunc porta hendrerit turpis, nec pharetra enim interdum id. Donec vel metus adipiscing tortor facilisis venenatis. Mauris vel volutpat leo. Nunc non justo nunc. Donec sapien arcu, egestas at facilisis et, interdum eget mauris. Nullam vitae bibendum mauris.</p>
</section>

<aside class="promo">
  <div class="promo-device" role="img" aria-label="Photo of an ADSL modem and network switch"></div>
  <div class="promo-strip"></div>
  <div class="promo-line promo-l1">ADSL2+</div>
  <div class="promo-line promo-l2">Unlimited</div>
  <div class="promo-line promo-l3">&amp; Phone Line</div>
  <div class="promo-line promo-l4">Rental</div>
  <div class="promo-line promo-l5">For Only</div>
  <div class="promo-line promo-price">$59.95</div>
  <div class="promo-cta">Click Here</div>
</aside>

<div class="footer-rule"></div>
<nav class="footer-nav">
  <a class="is-active">Home</a><span class="sep">|</span>
  <a>About Us</a><span class="sep">|</span>
  <a>Our Plans</a><span class="sep">|</span>
  <a>Contact Us</a><span class="sep">|</span>
  <a>Terms &amp; Condition</a><span class="sep">|</span>
  <a>Privacy</a><span class="sep">|</span>
  <a>Login</a>
</nav>
<div class="footer-brand"><span class="footer-brand-mark"></span>VELTRA</div>
<p class="copyright">Copyright © Veltra 2013. All rights reserved.</p>
<div class="bottom-bar"></div>

</body>
</html>
```